Design for sports training app

We need the design for 9 screens of an app that supports trainers of sport teams in preparing their training sessions. Regarding colors, fonts etc. there is absolute freedom for the designer to choose what he thinks is best.
The app will be called "Plomix", our idea for the logo is something like a stopwatch.
Wireframes are attached for every screen. You don't have to stick to those - if you have better ideas, we are happy to see them.
Our strategy is "mobile first". Based on the app design we will create a homepage later - I guess it makes sense to give this to the same person, let's see.
The deliverables are attached.
All in all the main target is to present a very simple, intuitive and nice UI that the user can work with without much learning.
Updates
Target Market(s)
Soccer trainers
Industry/Entity Type
Training
Look and feel

```html
<!DOCTYPE html>
<html lang="en">
<head>
<meta charset="utf-8">
<title>Plomix – Exercise Details</title>
<link href="https://fonts.googleapis.com/css2?family=Roboto:wght@300;400;500&family=Arimo:wght@400&display=swap" rel="stylesheet">
<style>
  :root{
    --page:#f1f1f2;
    --navy-top:#24435f;
    --navy-bottom:#10283f;
    --accent:#1f4a6b;
    --ink:#2b2f33;
    --body:#4a4f55;
    --muted:#9aa1a8;
    --rail:#e6eaee;
    --dots:#c5cacf;
    --link:#2d5b87;
    --tabbar:#f5f6f7;
    --icon-soft:#e9edf0;
    --icon-line:#8c99a5;
  }
  *{box-sizing:border-box;margin:0;padding:0}
  html,body{width:1188px;height:1200px;overflow:hidden;background:var(--page)}
  body{position:relative;font-family:"Roboto",sans-serif;color:var(--ink)}
  .page-title{position:absolute;top:36px;left:0;width:1188px;text-align:center;font-weight:300;font-size:23px;color:#333}
  .screen{position:absolute;top:214px;width:456px;height:812px;background:#fff;overflow:hidden;box-shadow:0 0 0 3px #111,0 8px 24px rgba(0,0,0,.12)}
  .screen--left{left:92px}
  .screen--right{left:632px}
  .app-header{position:absolute;top:0;left:0;width:100%;height:93px;background:linear-gradient(180deg,var(--navy-top),var(--navy-bottom));color:#fff}
  .status{position:absolute;top:9px;left:10px;right:12px;height:20px;font-size:15px;font-weight:400;display:flex;align-items:center}
  .status .signal{letter-spacing:-1px;font-size:12px;margin-right:6px}
  .status .carrier{display:flex;align-items:center;gap:6px}
  .status .time{position:absolute;left:0;right:0;text-align:center;pointer-events:none}
  .status .battery{margin-left:auto;display:flex;align-items:center;gap:6px}
  .nav-title{position:absolute;top:50px;left:0;width:100%;text-align:center;font-size:22px;font-weight:300}
  .nav-back{position:absolute;top:52px;left:18px}
  .rail{position:absolute;left:21px;top:93px;width:4px;height:651px;background:var(--rail)}
  .block-image{position:absolute;left:42px;width:401px}
  .hero{top:93px;height:103px;background:linear-gradient(180deg,#6f8f4e 0%,#4f7a34 60%,#3f6a2a 100%)}
  .video{top:390px;left:45px;width:398px;height:184px;background:linear-gradient(180deg,#4a4a4e 0%,#6b7a5a 35%,#4d7a35 100%)}
  .play{position:absolute;left:179px;top:73px}
  .divider{position:absolute;left:44px;width:400px;border-top:1.5px dotted var(--dots)}
  .node{position:absolute;left:9px;width:29px;height:29px;border-radius:50%;background:var(--icon-soft);display:flex;align-items:center;justify-content:center}
  .screen--right .node{background:var(--accent)}
  .node svg{stroke:var(--icon-line)}
  .screen--right .node svg{stroke:#fff}
  .exercise-title{position:absolute;left:44px;top:229px;font-size:19px;font-weight:300;color:var(--ink)}
  .copy{position:absolute;left:44px;width:400px;font-family:"Arimo",sans-serif;font-size:10.6px;line-height:15.8px;color:var(--body)}
  .copy--intro{top:259px}
  .copy--video{top:589px}
  .source{position:absolute;left:47px;top:665px;font-size:8px;color:var(--muted)}
  .source-link{position:absolute;left:47px;top:679px;font-size:11px;color:var(--link)}
  .source-note{position:absolute;left:47px;top:697px;font-size:11px;color:var(--body);font-family:"Arimo",sans-serif}
  .tabbar{position:absolute;left:0;bottom:0;width:100%;height:68px;background:var(--tabbar);border-top:1px solid #e3e6e9}
  .tab{position:absolute;top:10px;width:80px;text-align:center;font-size:11px;color:var(--muted)}
  .tab svg{display:block;margin:0 auto 6px;stroke:#a4acb3}
  .tab--active{color:var(--accent)}
  .tab--active svg{stroke:#6b8aa3}
  .tab--info{left:22px}
  .tab--skills{left:188px}
  .tab--preq{left:350px}
</style>
</head>
<body>
<h1 class="page-title">Screen4 &nbsp;– Exercise Details</h1>

<!-- variant with soft timeline icons -->
<section class="screen screen--left">
  <header class="app-header">
    <div class="status">
      <span class="carrier"><span class="signal">●●●○○</span>KITE
        <svg width="16" height="12" viewBox="0 0 16 12" fill="none" stroke="#fff" stroke-width="1.6"><path d="M1 4a10 10 0 0 1 14 0M3.5 6.5a6.5 6.5 0 0 1 9 0M6 9a3 3 0 0 1 4 0"/></svg></span>
      <span class="time">4:21 PM</span>
      <span class="battery">
        <svg width="8" height="14" viewBox="0 0 8 14" fill="none" stroke="#9fb0c0" stroke-width="1.1"><path d="M1 4l6 6-3 3V1l3 3-6 6"/></svg>22%
        <svg width="34" height="14" viewBox="0 0 34 14" fill="none"><rect x="0.6" y="0.6" width="29" height="12.8" rx="2.5" stroke="#fff" stroke-width="1.2"/><rect x="2.5" y="2.5" width="6" height="9" fill="#fff"/><rect x="31" y="4.5" width="2" height="5" fill="#fff"/></svg>
      </span>
    </div>
    <svg class="nav-back" width="12" height="22" viewBox="0 0 12 22" fill="none" stroke="#fff" stroke-width="1.6"><path d="M11 1L1 11l10 10"/></svg>
    <div class="nav-title">Offensive 2 vs. 1</div>
  </header>

  <div class="rail"></div>
  <div class="block-image hero" role="img" aria-label="Photo of a soccer player in a yellow shirt on a green pitch"></div>
  <div class="divider" style="top:216px"></div>

  <div class="node" style="top:226px"><svg width="15" height="15" viewBox="0 0 15 15" fill="none" stroke-width="1.2"><path d="M8 2H2v11h11V7"/><path d="M6 9l1-3 6-5 1.5 1.5-6 5z"/></svg></div>
  <h2 class="exercise-title">Offensive 2 vs. 1</h2>
  <p class="copy copy--intro">Lorem ipsum dolor sit amet, consectetur adipisicing elit, sed do eiusmod tempor incidi dunt&nbsp; labore et dolore magna aliqua. Ut enim ad minim veniam, quis nost ex ercitation ullamco laboris nisi ut aliquip ex ea commodo consequat. Duis aute irure dolor in repr ehenderit in vluptate velit esse cillum dolore eu fugiat nulla par atur eaque ipsa quae ab illo inventore veritatis et quasi architecto beatae vitae dictasunt explicabo nemo enim ipsam voluptatem.</p>
  <div class="divider" style="top:370px"></div>

  <div class="node" style="top:381px"><svg width="16" height="14" viewBox="0 0 16 14" fill="none" stroke-width="1.1"><rect x="1" y="1" width="14" height="12"/><path d="M4 1v12M12 1v12M1 4h3M1 7h3M1 10h3M12 4h3M12 7h3M12 10h3M7 5l2.5 2L7 9z"/></svg></div>
  <div class="block-image video" role="img" aria-label="Video still of a team doing a warm-up drill on the training pitch">
    <svg class="play" width="40" height="40" viewBox="0 0 40 40"><circle cx="20" cy="20" r="20" fill="rgba(255,255,255,.25)"/><path d="M15 11l13 9-13 9z" fill="none" stroke="#fff" stroke-width="1.6"/></svg>
  </div>
  <p class="copy copy--video">Adipisicing elit, sed do eiusmod tempor incidi dunt&nbsp; labore et dolore magna aliqua. Ut enim ad minim veniam, quis nost ex ercitation ullamco laboris nisi ut aliquip ex ea commodo consequat.</p>
  <div class="divider" style="top:650px"></div>

  <div class="node" style="top:660px"><svg width="16" height="16" viewBox="0 0 16 16" fill="none" stroke-width="1.3"><path d="M7 9l2-2M6 6.5L3.5 9a2.4 2.4 0 0 0 3.4 3.4L9.5 10M10 9.5L12.5 7a2.4 2.4 0 0 0-3.4-3.4L6.5 6"/></svg></div>
  <div class="source">Filecrate, Shrtn</div>
  <div class="source-link">http://shrtn.io/7kqPwa</div>
  <div class="source-note">Dolore magna aliquat enim ad minim veniam,</div>

  <nav class="tabbar">
    <div class="tab tab--info tab--active"><svg width="20" height="24" viewBox="0 0 20 24" fill="none" stroke-width="1.2"><rect x="1" y="3" width="18" height="20"/><rect x="6" y="1" width="8" height="4"/><path d="M4 9h12M4 12h12M4 15h12M4 18h8"/></svg>Info</div>
    <div class="tab tab--skills"><svg width="24" height="24" viewBox="0 0 24 24" fill="none" stroke-width="1.2"><path d="M8 15a6 6 0 1 1 8 0v3H8z"/><path d="M9 20h6M10 22h4M12 1v2M3 4l1.5 1.5M21 4l-1.5 1.5M1 12h2M21 12h2"/></svg>Skills</div>
    <div class="tab tab--preq"><svg width="26" height="24" viewBox="0 0 26 24" fill="none" stroke-width="1.2"><path d="M13 2l11 6-11 6L2 8z"/><path d="M2 12l11 6 11-6M2 16l11 6 11-6"/></svg>Preq</div>
  </nav>
</section>

<!-- variant with filled timeline icons -->
<section class="screen screen--right">
  <header class="app-header">
    <div class="status">
      <span class="carrier"><span class="signal">●●●○○</span>KITE
        <svg width="16" height="12" viewBox="0 0 16 12" fill="none" stroke="#fff" stroke-width="1.6"><path d="M1 4a10 10 0 0 1 14 0M3.5 6.5a6.5 6.5 0 0 1 9 0M6 9a3 3 0 0 1 4 0"/></svg></span>
      <span class="time">4:21 PM</span>
      <span class="battery">
        <svg width="8" height="14" viewBox="0 0 8 14" fill="none" stroke="#9fb0c0" stroke-width="1.1"><path d="M1 4l6 6-3 3V1l3 3-6 6"/></svg>22%
        <svg width="34" height="14" viewBox="0 0 34 14" fill="none"><rect x="0.6" y="0.6" width="29" height="12.8" rx="2.5" stroke="#fff" stroke-width="1.2"/><rect x="2.5" y="2.5" width="6" height="9" fill="#fff"/><rect x="31" y="4.5" width="2" height="5" fill="#fff"/></svg>
      </span>
    </div>
    <svg class="nav-back" width="12" height="22" viewBox="0 0 12 22" fill="none" stroke="#fff" stroke-width="1.6"><path d="M11 1L1 11l10 10"/></svg>
    <div class="nav-title">Offensive 2 vs. 1</div>
  </header>

  <div class="rail"></div>
  <div class="block-image hero" role="img" aria-label="Photo of a soccer player in a yellow shirt on a green pitch"></div>
  <div class="divider" style="top:216px"></div>

  <div class="node" style="top:226px"><svg width="15" height="15" viewBox="0 0 15 15" fill="none" stroke-width="1.2"><path d="M8 2H2v11h11V7"/><path d="M6 9l1-3 6-5 1.5 1.5-6 5z"/></svg></div>
  <h2 class="exercise-title">Offensive 2 vs. 1</h2>
  <p class="copy copy--intro">Lorem ipsum dolor sit amet, consectetur adipisicing elit, sed do eiusmod tempor incidi dunt&nbsp; labore et dolore magna aliqua. Ut enim ad minim veniam, quis nost ex ercitation ullamco laboris nisi ut aliquip ex ea commodo consequat. Duis aute irure dolor in repr ehenderit in vluptate velit esse cillum dolore eu fugiat nulla par atur eaque ipsa quae ab illo inventore veritatis et quasi architecto beatae vitae dictasunt explicabo nemo enim ipsam voluptatem.</p>
  <div class="divider" style="top:370px"></div>

  <div class="node" style="top:381px"><svg width="16" height="14" viewBox="0 0 16 14" fill="none" stroke-width="1.1"><rect x="1" y="1" width="14" height="12"/><path d="M4 1v12M12 1v12M1 4h3M1 7h3M1 10h3M12 4h3M12 7h3M12 10h3M7 5l2.5 2L7 9z"/></svg></div>
  <div class="block-image video" role="img" aria-label="Video still of a team doing a warm-up drill on the training pitch">
    <svg class="play" width="40" height="40" viewBox="0 0 40 40"><circle cx="20" cy="20" r="20" fill="rgba(255,255,255,.25)"/><path d="M15 11l13 9-13 9z" fill="none" stroke="#fff" stroke-width="1.6"/></svg>
  </div>
  <p class="copy copy--video">Adipisicing elit, sed do eiusmod tempor incidi dunt&nbsp; labore et dolore magna aliqua. Ut enim ad minim veniam, quis nost ex ercitation ullamco laboris nisi ut aliquip ex ea commodo consequat.</p>
  <div class="divider" style="top:650px"></div>

  <div class="node" style="top:660px"><svg width="16" height="16" viewBox="0 0 16 16" fill="none" stroke-width="1.3"><path d="M7 9l2-2M6 6.5L3.5 9a2.4 2.4 0 0 0 3.4 3.4L9.5 10M10 9.5L12.5 7a2.4 2.4 0 0 0-3.4-3.4L6.5 6"/></svg></div>
  <div class="source">Filecrate, Shrtn</div>
  <div class="source-link">http://shrtn.io/7kqPwa</div>
  <div class="source-note">Dolore magna aliquat enim ad minim veniam,</div>

  <nav class="tabbar">
    <div class="tab tab--info tab--active"><svg width="20" height="24" viewBox="0 0 20 24" fill="none" stroke-width="1.2"><rect x="1" y="3" width="18" height="20"/><rect x="6" y="1" width="8" height="4"/><path d="M4 9h12M4 12h12M4 15h12M4 18h8"/></svg>Info</div>
    <div class="tab tab--skills"><svg width="24" height="24" viewBox="0 0 24 24" fill="none" stroke-width="1.2"><path d="M8 15a6 6 0 1 1 8 0v3H8z"/><path d="M9 20h6M10 22h4M12 1v2M3 4l1.5 1.5M21 4l-1.5 1.5M1 12h2M21 12h2"/></svg>Skills</div>
    <div class="tab tab--preq"><svg width="26" height="24" viewBox="0 0 26 24" fill="none" stroke-width="1.2"><path d="M13 2l11 6-11 6L2 8z"/><path d="M2 12l11 6 11-6M2 16l11 6 11-6"/></svg>Preq</div>
  </nav>
</section>
</body>
</html>
```